KQW Authorised Dealer needs Business Cards

We need a business card designed for our branch owners. Vellmor Alarms is an Authorised KQW Dealer and does its own independent installations outside of the KQW work we perform so whilst the KQW Authorised Dealer Logo needs to be included, it should not be overwhelming in respect of the overall look of the card. I would like a rounded edge to the cards corners rather than a 90 degree hard edge. We also need to promote the fact that we do First Class Alarm & CCTV Solutions. (Details of card holder to follow)

```html
<!DOCTYPE html>
<html lang="en">
<head>
<meta charset="utf-8">
<title>Vellmor Alarms – Business Card</title>
<link rel="stylesheet" href="https://fonts.googleapis.com/css2?family=Oswald:wght@600&family=Open+Sans:wght@400;600&display=swap">
<style>
  :root {
    --page-bg: #e6e6e4;
    --card-white: #ffffff;
    --brand-blue: #1f74b9;
    --brand-blue-deep: #1766a8;
    --charcoal: #3b3d40;
    --ink: #2f3033;
    --text-light: #ffffff;
  }
  * { box-sizing: border-box; margin: 0; padding: 0; }
  html, body {
    width: 1200px; height: 900px; overflow: hidden;
    background: var(--page-bg);
    font-family: "Open Sans", Arial, sans-serif;
  }
  .canvas { position: relative; width: 1200px; height: 900px; }
  .card {
    position: absolute; left: 280px;
    width: 640px; height: 366px;
    background: var(--card-white);
    border-radius: 18px;
    overflow: hidden;
    box-shadow: 0 6px 18px rgba(0,0,0,0.15);
  }
  .card-front { top: 60px; }
  .card-back { top: 474px; }
  .card-shapes { position: absolute; inset: 0; }

  .brand { position: absolute; }
  .brand-lockup { display: flex; align-items: center; gap: 12px; }
  .brand-mark { width: 34px; height: 34px; background: var(--brand-blue); flex: none; }
  .brand-name {
    font-family: "Oswald", "Arial Narrow", sans-serif;
    font-weight: 600; font-size: 40px; letter-spacing: 0.5px;
    text-transform: uppercase; color: var(--brand-blue); line-height: 1;
    white-space: nowrap;
  }
  .brand-tagline {
    margin-top: 10px;
    font-size: 13px; font-weight: 600; letter-spacing: 0.3px;
    color: var(--ink); white-space: nowrap;
  }
  .card-front .brand { left: 70px; top: 150px; }
  .card-back .brand { left: 40px; top: 160px; }
  .card-back .brand-mark { width: 28px; height: 28px; }
  .card-back .brand-name { font-size: 32px; }

  .partner-badge {
    position: absolute; right: 52px; top: 48px;
    width: 96px; height: 96px; border-radius: 50%;
    background: var(--brand-blue-deep);
  }

  .holder {
    position: absolute; left: 330px; top: 30px;
    width: 180px; padding: 8px 18px 8px 22px;
    background: var(--card-white);
  }
  .holder-name { font-size: 21px; font-weight: 400; color: var(--brand-blue); line-height: 1.2; white-space: nowrap; }
  .holder-role { font-size: 13px; font-weight: 600; color: var(--ink); }

  .contact {
    position: absolute; left: 385px; top: 128px;
    color: var(--text-light); font-size: 15px; line-height: 1.45;
    list-style: none;
  }
  .contact-address { margin-bottom: 12px; letter-spacing: 0.5px; }
  .contact li { display: flex; align-items: center; gap: 10px; white-space: nowrap; }
  .contact svg { width: 15px; height: 15px; flex: none; }
</style>
</head>
<body>
<main class="canvas">

  <section class="card card-front" aria-label="Card front">
    <svg class="card-shapes" viewBox="0 0 640 366" preserveAspectRatio="none" aria-hidden="true">
      <rect x="0" y="0" width="640" height="24" fill="var(--charcoal)"/>
      <polygon points="0,366 0,336 640,176 640,366" fill="var(--brand-blue)"/>
    </svg>
    <div class="brand">
      <div class="brand-lockup">
        <span class="brand-mark"></span>
        <span class="brand-name">Vellmor Alarms</span>
      </div>
    </div>
    <div class="partner-badge" role="img" aria-label="KQW authorised dealer badge"></div>
  </section>

  <section class="card card-back" aria-label="Card back">
    <svg class="card-shapes" viewBox="0 0 640 366" preserveAspectRatio="none" aria-hidden="true">
      <polygon points="330,0 640,0 640,366 380,366" fill="var(--brand-blue)"/>
    </svg>
    <div class="brand">
      <div class="brand-lockup">
        <span class="brand-mark"></span>
        <span class="brand-name">Vellmor Alarms</span>
      </div>
      <p class="brand-tagline">First Class Alarm &amp; CCTV Solutions</p>
    </div>
    <div class="holder">
      <p class="holder-name">Dana Pryce</p>
      <p class="holder-role">Manager</p>
    </div>
    <ul class="contact">
      <li class="contact-address">PO Box 480 Harlow,<br>2041 Elmara</li>
      <li>
        <svg viewBox="0 0 16 16" aria-hidden="true"><path d="M3.5 1.5l2.5 2.8-1.4 1.8c.9 2 2.5 3.6 4.5 4.5l1.8-1.4 2.8 2.5-1.6 2.3C7.5 13.8 2.2 8.5 1.2 3.1z" fill="#fff"/></svg>
        041 786 2290
      </li>
      <li>
        <svg viewBox="0 0 16 16" aria-hidden="true"><rect x="4" y="1" width="8" height="14" rx="1.5" fill="none" stroke="#fff" stroke-width="1.5"/><rect x="5.5" y="3" width="5" height="6" fill="#fff"/><circle cx="8" cy="12.5" r="1" fill="#fff"/></svg>
        082 614 3357
      </li>
      <li>
        <svg viewBox="0 0 16 16" aria-hidden="true"><rect x="1" y="3" width="14" height="10" fill="none" stroke="#fff" stroke-width="1.5"/><path d="M1 3l7 6 7-6" fill="none" stroke="#fff" stroke-width="1.5"/></svg>
        info@vellmoralarms.com
      </li>
      <li>
        <svg viewBox="0 0 16 16" aria-hidden="true"><circle cx="8" cy="8" r="6.5" fill="none" stroke="#fff" stroke-width="1.4"/><ellipse cx="8" cy="8" rx="2.8" ry="6.5" fill="none" stroke="#fff" stroke-width="1.2"/><path d="M1.5 8h13M2.5 5h11M2.5 11h11" stroke="#fff" stroke-width="1.1"/></svg>
        www.vellmoralarms.com
      </li>
    </ul>
  </section>

</main>
</body>
</html>
```